Design für Zeitungsanzeige hochwertige Betten
Zielgruppe
Ruhepunkt Sana verkauft hochwertige Bettsystem für schmerzfreies Liegen und Schlafen. Die Kunden (40+) kommen in das Geschäft, weil sie Rückenschmerzen haben und nicht gut schlafen können. Dort werden Sie individuell beraten. Ruhepunkt Sana hat einen Expertenstatus rum um das Thema Liegen und Schlafen, da Sie maßgeschneiderte Matratzen mit Hilfe von Liegedruckmessung anbieten. Die Produkte sind frei von Chemie und Pestiziden, was positiv zum guten Schlaf beiträgt. Somit sind die Produkte auch sehr hochwertig, aber auch kostspielig.
Aufgabenstellung
Gern einmal auf die Seite:
http://www.ruhepunkt-lindenau.de/traumbetten/
http://www.ruhepunkt-sana.com/betten/
-Vorher / nachher Bilder sind sehr effektvoll
-Unbedingt in die Anzeigen nehmen: Adresse- Logo Firma, "Ergonomische Betten" soll mit auf der Anzeige sein und vom Stil ähnlich zu der Schuhanzeige aufgebaut sein.
- gerne auch Unten mit GUTSCHEIN und einer Schere: Kostenlose Liegedruck-Messung
- Zielgruppe 40+
- ein Bett im Hintergrund würde sinnmachen, wenn eine Person davor steht und sich den Rücken hält.
- In der Art wollen wir auch die Anzeige haben. Gut wäre wenn eine ältere Dame zusehen ist, die genau der Zielgruppe entspricht.
Allgemeines:
- Die hohe Qualität der Produkte soll im Vordergrund stehen und die richtige Zielgruppe mit dem passenden Kleingeld ansprechen.
- Das Ruhepunkt Sana Logo muss zusehen sein und auffallen, da dieses sich bei den Menschen einprägen soll.
- Kunden sollen aufgefordert werden zu Ruhepunkt Sana ins Geschäft zu kommen und Ruhepunkt Sana als Experte und Berater soll im Vordergrund stehen.
- Adresse mit Ort muss zusehen sein.
Eine Zeitungsanzeige 4-farbig
Maße: querformat 5*9 cm (und vllt hochformat 4,5*14cm)

```html
<!DOCTYPE html>
<html lang="de">
<head>
<meta charset="utf-8">
<title>Ruhepunkt Sana – Anzeigen</title>
<link rel="stylesheet" href="https://fonts.googleapis.com/css2?family=Crimson+Pro:wght@400&family=Fira+Sans:wght@700&family=Lato:wght@300;400;700;900&display=swap">
<style>
  :root {
    --wine: #7a2a2e;
    --badge: #6e2533;
    --green: #6cb33f;
    --grey: #6d6d6d;
    --text-grey: #5f5f5f;
    --frame: #555;
    --cream: #f3ede4;
    --warm: #e2d3be;
    --deep-warm: #cdb89c;
    --skin: #d9b497;
  }
  * { margin: 0; padding: 0; box-sizing: border-box; }
  html, body { width: 1200px; height: 981px; overflow: hidden; background: #fff; }
  body { position: relative; font-family: "Lato", sans-serif; }

  .format-label {
    position: absolute;
    font-family: "Crimson Pro", serif;
    font-size: 23px;
    color: #222;
    white-space: nowrap;
  }
  .format-label--tall { left: 156px; top: 62px; }
  .format-label--wide { left: 623px; top: 198px; }

  .ad {
    position: absolute;
    border: 1px solid var(--frame);
    background: #fff;
    overflow: hidden;
  }
  .ad--tall { left: 157px; top: 118px; width: 259px; height: 808px; }
  .ad--wide { left: 480px; top: 255px; width: 519px; height: 289px; }

  .photo { position: absolute; left: 0; width: 100%; }
  .ad--tall .photo--before {
    top: 0; height: 160px;
    background:
      radial-gradient(ellipse 70px 55px at 68% 35%, rgba(217,180,151,.75), rgba(217,180,151,0) 100%),
      radial-gradient(ellipse 120px 60px at 40% 70%, rgba(255,255,255,.9), rgba(255,255,255,0) 100%),
      linear-gradient(180deg, var(--warm) 0%, var(--cream) 60%, #fff 100%);
  }
  .ad--tall .photo--glow {
    top: 640px; height: 168px;
    background: linear-gradient(180deg, #fff 0%, var(--cream) 100%);
  }
  .ad--tall .photo--after {
    top: 690px; height: 118px;
    background:
      radial-gradient(ellipse 40px 32px at 62% 30%, rgba(217,180,151,.85), rgba(217,180,151,0) 100%),
      radial-gradient(ellipse 150px 40px at 50% 95%, rgba(255,255,255,.95), rgba(255,255,255,0) 100%),
      linear-gradient(180deg, rgba(243,237,228,0) 0%, var(--warm) 45%, var(--deep-warm) 100%);
  }
  .ad--wide .photo--after {
    top: 0; height: 289px;
    background:
      radial-gradient(ellipse 70px 55px at 76% 78%, rgba(217,180,151,.9), rgba(217,180,151,0) 100%),
      radial-gradient(ellipse 260px 40px at 60% 102%, rgba(255,255,255,.95), rgba(255,255,255,0) 100%),
      linear-gradient(180deg, #fff 0%, #fff 28%, var(--cream) 55%, var(--warm) 82%, var(--deep-warm) 100%);
  }

  .questions {
    position: absolute;
    font-family: "Fira Sans", sans-serif;
    font-weight: 700;
    color: var(--wine);
  }
  .ad--tall .questions { left: 31px; top: 141px; font-size: 19px; line-height: 29px; }
  .ad--wide .questions { left: 25px; top: 17px; font-size: 16px; line-height: 24px; }

  .dotted-path { position: absolute; left: 0; top: 0; overflow: visible; }

  .invitation {
    position: absolute;
    font-family: "Fira Sans", sans-serif;
    font-weight: 700;
    color: var(--grey);
    text-align: right;
  }
  .ad--tall .invitation { right: 30px; top: 309px; font-size: 20px; line-height: 30px; }
  .ad--wide .invitation { right: 257px; top: 98px; font-size: 16px; line-height: 24px; }

  .badge { position: absolute; }
  .ad--tall .badge { left: 97px; top: 377px; width: 149px; height: 149px; }
  .ad--wide .badge { left: 19px; top: 148px; width: 123px; height: 123px; }

  .brand { position: absolute; text-align: center; }
  .ad--tall .brand { left: 0; width: 100%; top: 546px; }
  .ad--wide .brand { left: 297px; width: 200px; top: 26px; }

  .brand-name {
    font-family: "Lato", sans-serif;
    font-weight: 900;
    color: var(--wine);
    white-space: nowrap;
    line-height: 1;
  }
  .ad--tall .brand-name { font-size: 29px; margin-bottom: 22px; }
  .ad--wide .brand-name { font-size: 28px; margin-bottom: 19px; }

  .address {
    font-style: normal;
    font-weight: 400;
    color: var(--text-grey);
  }
  .ad--tall .address { font-size: 13.5px; line-height: 19px; }
  .ad--wide .address { font-size: 13px; line-height: 18.5px; }

  .phone {
    font-family: "Lato", sans-serif;
    font-weight: 900;
    letter-spacing: -0.6px;
    white-space: nowrap;
    line-height: 1;
  }
  .ad--tall .phone { font-size: 26px; margin-top: 14px; }
  .ad--wide .phone { font-size: 26px; margin-top: 12px; }
  .phone-area { color: var(--green); margin-right: 7px; }
  .phone-number { color: var(--wine); }
</style>
</head>
<body>

<p class="format-label format-label--tall">Format: hoch, 4,5x14 cm</p>
<p class="format-label format-label--wide">Format: quer, 9x5 cm</p>

<section class="ad ad--tall">
  <div class="photo photo--before" role="img" aria-label="Mann im Bett, der sich mit schmerzverzerrtem Gesicht den Rücken hält"></div>
  <div class="photo photo--glow" aria-hidden="true"></div>
  <div class="photo photo--after" role="img" aria-label="Entspannter, lächelnder Mann im Bett mit Händen hinter dem Kopf"></div>

  <p class="questions">Unausgeschlafen?<br>Rückenschmerzen?<br>Steifer Hals?</p>

  <svg class="dotted-path" width="259" height="320" aria-hidden="true">
    <polyline points="77,236 77,269 160,269 160,299" fill="none" stroke="var(--green)" stroke-width="2.6" stroke-dasharray="0.1 7" stroke-linecap="round"/>
  </svg>

  <p class="invitation">Wollen Sie daran<br>etwas ändern?</p>

  <svg class="badge" viewBox="0 0 148 148" aria-label="Wir nehmen uns Zeit! Vorbeikommen, Beraten lassen, Probeliegen">
    <circle cx="74" cy="74" r="74" fill="var(--badge)"/>
    <g transform="rotate(-10 74 74)" fill="#fff" font-family="Lato, sans-serif">
      <text x="74" y="44" text-anchor="middle" font-size="16" font-weight="700">Wir nehmen</text>
      <text x="70" y="66" text-anchor="middle" font-size="16" font-weight="700">uns Zeit!</text>
      <g font-size="13" font-weight="400">
        <circle cx="19" cy="88" r="5" fill="var(--green)"/>
        <path d="M16.5 88 l2 2 l3.5 -4" stroke="#fff" stroke-width="1.5" fill="none"/>
        <text x="28" y="92">Vorbeikommen</text>
        <circle cx="23" cy="106" r="5" fill="var(--green)"/>
        <path d="M20.5 106 l2 2 l3.5 -4" stroke="#fff" stroke-width="1.5" fill="none"/>
        <text x="32" y="110">Beraten lassen</text>
        <circle cx="31" cy="124" r="5" fill="var(--green)"/>
        <path d="M28.5 124 l2 2 l3.5 -4" stroke="#fff" stroke-width="1.5" fill="none"/>
        <text x="40" y="128">Probeliegen</text>
      </g>
    </g>
  </svg>

  <div class="brand">
    <p class="brand-name">Ruhepunkt Sana</p>
    <address class="address">Ruhepunkt Sana<br>Lindenweg 7<br>04177 Lindenau</address>
    <p class="phone"><span class="phone-area">04103</span><span class="phone-number">55 18 20</span></p>
  </div>
</section>

<section class="ad ad--wide">
  <div class="photo photo--after" role="img" aria-label="Entspannter, lächelnder Mann im Bett mit Händen hinter dem Kopf"></div>

  <p class="questions">Unausgeschlafen?<br>Rückenschmerzen?<br>Steifer Hals?</p>

  <svg class="dotted-path" width="519" height="289" aria-hidden="true">
    <polyline points="78,97 78,131 144,131" fill="none" stroke="var(--green)" stroke-width="2.2" stroke-dasharray="0.1 5" stroke-linecap="round"/>
  </svg>

  <p class="invitation">Wollen Sie daran<br>etwas ändern?</p>

  <svg class="badge" viewBox="0 0 148 148" aria-label="Wir nehmen uns Zeit! Vorbeikommen, Beraten lassen, Probeliegen">
    <circle cx="74" cy="74" r="74" fill="var(--badge)"/>
    <g transform="rotate(-10 74 74)" fill="#fff" font-family="Lato, sans-serif">
      <text x="74" y="44" text-anchor="middle" font-size="16" font-weight="700">Wir nehmen</text>
      <text x="70" y="66" text-anchor="middle" font-size="16" font-weight="700">uns Zeit!</text>
      <g font-size="13" font-weight="400">
        <circle cx="19" cy="88" r="5" fill="var(--green)"/>
        <path d="M16.5 88 l2 2 l3.5 -4" stroke="#fff" stroke-width="1.5" fill="none"/>
        <text x="28" y="92">Vorbeikommen</text>
        <circle cx="23" cy="106" r="5" fill="var(--green)"/>
        <path d="M20.5 106 l2 2 l3.5 -4" stroke="#fff" stroke-width="1.5" fill="none"/>
        <text x="32" y="110">Beraten lassen</text>
        <circle cx="31" cy="124" r="5" fill="var(--green)"/>
        <path d="M28.5 124 l2 2 l3.5 -4" stroke="#fff" stroke-width="1.5" fill="none"/>
        <text x="40" y="128">Probeliegen</text>
      </g>
    </g>
  </svg>

  <div class="brand">
    <p class="brand-name">Ruhepunkt Sana</p>
    <address class="address">Ruhepunkt Sana<br>Lindenweg 7<br>04177 Lindenau</address>
    <p class="phone"><span class="phone-area">04103</span><span class="phone-number">55 18 20</span></p>
  </div>
</section>

</body>
</html>
```